Letterhead Design Project

Consulting Company , we want a letterhead incorporating both the picture provided and the logo provided. The font name is monotype corsiva.
Target Market(s)
Dentist
Industry/Entity Type
Consulting
Font styles to use
Other font styles liked:
- monotype corsiva

Colors
0455a3
Requirements
Must have
- the logo, the picture (see attached), the website name, the email. and the phone numbers.
- Website: www.trquillarisadvisory.solutions
- Email: will be provided to the winner, please use placeholder
- Phone numbers:
- Petra Hallum 5829017763
- Owen Vrastik 6148250397

Nice to have
- a swoop or wave across the bottom. a line up the side. I don't know guys. design something unique and professional.

Should not have
- arrows pointing off the logo or anywhere. no arrows. our logo altered in anyway. no broken circles. no variences in blue. we like our logo the way it is. the font is monotype corsiva

```html
<!DOCTYPE html>
<html lang="en">
<head>
<meta charset="utf-8">
<title>Trquillaris Advisory Letterhead</title>
<link rel="stylesheet" href="https://fonts.googleapis.com/css2?family=Cormorant+Garamond:ital,wght@1,500;1,600&family=Source+Sans+3:wght@400;600;700&display=swap">
<style>
  :root {
    --brand-blue: #0b56a4;
    --backdrop: #4a4a4a;
    --paper: #ffffff;
    --ink: #555555;
    --ink-dark: #111111;
    --photo-light: #d9d9d9;
    --photo-dark: #3a3a3a;
  }
  * { margin: 0; padding: 0; box-sizing: border-box; }
  html, body { width: 999px; height: 1200px; overflow: hidden; }
  body { background: var(--backdrop); position: relative; font-family: "Source Sans 3", Arial, sans-serif; }

  .letterhead {
    position: absolute; left: 71px; top: 45px; width: 857px; height: 1110px;
    background: var(--paper); overflow: hidden;
  }
  .header-lines { position: absolute; left: 0; top: 0; }
  .brand-circle {
    position: absolute; left: 61px; top: 57px; width: 89px; height: 89px;
    border: 5px solid var(--brand-blue); border-radius: 50%;
  }
  .company-name {
    position: absolute; left: 164px; top: 92px;
    font-family: "Source Sans 3", Arial, sans-serif; font-weight: 600;
    font-size: 20px; color: var(--brand-blue); white-space: nowrap;
  }
  .company-address {
    position: absolute; left: 162px; top: 119px;
    font-family: "Cormorant Garamond", Georgia, serif; font-style: italic; font-weight: 600;
    font-size: 13px; line-height: 18px; color: var(--ink-dark);
  }

  .letter-body { position: absolute; left: 73px; top: 262px; width: 712px; color: var(--ink); }
  .letter-title { font-size: 21px; font-weight: 700; line-height: 28px; margin-bottom: 8px; }
  .letter-intro { font-size: 15px; line-height: 20px; margin-bottom: 40px; }
  .letter-body p.copy { font-size: 15px; line-height: 20px; text-align: justify; margin-bottom: 20px; }

  .contact-web {
    position: absolute; left: 64px; top: 1027px;
    font-family: "Cormorant Garamond", Georgia, serif; font-style: italic; font-weight: 600;
    font-size: 14.5px; line-height: 20px; color: var(--ink-dark);
  }
  .signatory-name {
    position: absolute; left: 443px; top: 990px;
    font-family: "Cormorant Garamond", Georgia, serif; font-style: italic; font-weight: 500;
    font-size: 38px; color: var(--brand-blue); white-space: nowrap;
  }
  .signatory-phone {
    position: absolute; left: 447px; top: 1037px;
    font-family: "Cormorant Garamond", Georgia, serif; font-style: italic; font-weight: 600;
    font-size: 22px; color: var(--ink-dark); letter-spacing: 0.5px;
  }
  .footer-band {
    position: absolute; left: 0; top: 1071px; width: 857px; height: 39px; background: var(--brand-blue);
  }
  .portrait-frame {
    position: absolute; left: 633px; top: 863px; width: 164px; height: 220px;
    border: 6px solid var(--brand-blue); border-radius: 50%; background: var(--paper);
    padding: 5px;
  }
  .portrait-photo {
    width: 100%; height: 100%; border-radius: 50%;
    background: radial-gradient(ellipse at 50% 40%, var(--photo-light) 0%, #a8a8a8 45%, var(--photo-dark) 100%);
  }
</style>
</head>
<body>
  <div class="letterhead">
    <svg class="header-lines" width="857" height="90" viewBox="0 0 857 90" aria-hidden="true">
      <polygon points="132,57 382,57 386,61 132,61" fill="var(--brand-blue)"/>
      <polygon points="147,69 565,69 569,74 147,74" fill="var(--brand-blue)"/>
      <polygon points="157,80 853,80 857,85 157,85" fill="var(--brand-blue)"/>
    </svg>
    <div class="brand-circle"></div>
    <div class="company-name">Trquillaris Advisory, LLC</div>
    <div class="company-address">418 Alder Lane<br>Marlow Springs, Ohio 43390</div>

    <div class="letter-body">
      <h1 class="letter-title">Lorem ipsum dolor sit amet</h1>
      <p class="letter-intro">Lorem ipsum dolor sit amet,<br>consectetur adipiscing elit.</p>
      <p class="copy">Lorem ipsum dolor sit amet, consectetur adipiscing elit. Integer eu odio mattis, pulvinar turpis quis, faucibus nisl. Proin feugiat, erat vitae cursus pharetra, enim est semper ligula, in malesuada orci nisl et diam. Etiam elementum metus ac fringilla vulputate. Etiam mattis ligula sed ante mollis bibendum. Orci varius natoque penatibus et magnis dis parturient montes, nascetur ridiculus mus.</p>
      <p class="copy">Ut nibh augue, blandit ac orci ac, rutrum congue enim. Suspendisse gravida vulputate felis, quis interdum orci tincidunt quis. Praesent imperdiet maximus neque. Mauris ut dui enim. Nullam at efficitur elit. Donec ante ipsum, fermentum at lectus vel, blandit vulputate ante. Proin luctus suscipit diam id vestibulum. Morbi malesuada id mauris eget ullamcorper.</p>
      <p class="copy">Donec varius orci purus, vitae aliquam libero volutpat id. Integer sed imperdiet libero. Aliquam accumsan, risus sit amet ornare consectetur, turpis felis dictum justo, non rhoncus mauris dui sed velit. Pellentesque habitant morbi tristique senectus et netus et malesuada fames ac turpis egestas. Pellentesque tincidunt vitae ligula nec imperdiet. Donec sed congue enim. Nullam elementum faucibus nulla nec vestibulum. Sed at tempor ligula. In quis vulputate nunc. Integer at gravida lacus, ac tristique risus. Sed at vulputate nulla.</p>
      <p class="copy">Praesent blandit nunc eu efficitur commodo. In tempor nisi ex, vel venenatis ante vestibulum a. Duis vestibulum nibh a erat sagittis, nec euismod lorem varius. Nam ultricies turpis sed justo sollicitudin volutpat. Morbi sed mollis eros. Sed quis tortor id enim vehicula porttitor. Curabitur non aliquam ex. Phasellus dignissim fermentum elit, at finibus ligula mattis eget.</p>
    </div>

    <div class="contact-web">info@trquillarisadvisory.solutions<br>www.trquillarisadvisory.solutions</div>
    <div class="signatory-name">Petra Hallum</div>
    <div class="signatory-phone">5829017763</div>
    <div class="footer-band"></div>
    <div class="portrait-frame">
      <div class="portrait-photo" role="img" aria-label="Black and white portrait photo of Petra Hallum"></div>
    </div>
  </div>
</body>
</html>
```